New Innovative Counselling and psychotherapy Service needs Business Card design

Keep it simple and professional. On one side, just company name and logo (perhaps in all blue) and maybe a tag line.

On other side (all white) my name and Qualifications in centre

Industry/Entity Type

Health And Wellness

Contact Information for Business Card

Derek Hollis
Counsellor & Psychotherapist
BSc (Psychol.), BA, Dip. (Couns. & Psych.), PG.Cert (CBT), MGVrA, NWTF

I will also require Mobile no, Email and web site address of which I'll pass on to final designer.

Font styles to use
Sans Serif

Requirements
Must have
• My Logo Only and please use the colours in logo that is in it.
Should not have
• Any other images

```html
<!DOCTYPE html>
<html lang="en">
<head>
<meta charset="utf-8">
<title>Harbor Lane – Business Card</title>
<link href="https://fonts.googleapis.com/css2?family=Lato:wght@300;400;700&display=swap" rel="stylesheet">
<style>
  :root {
    --brand-blue: #4fb0e3;
    --ink: #1d1d1d;
    --muted: #9a9a9a;
    --paper: #ffffff;
    --backdrop: #eef0f2;
    --edge: #e2e4e6;
  }
  * { margin: 0; padding: 0; box-sizing: border-box; }
  html, body {
    width: 1200px; height: 1200px; overflow: hidden;
    background: var(--backdrop);
    font-family: "Lato", sans-serif;
  }
  .sheet {
    position: relative; width: 1200px; height: 1200px;
    display: flex; align-items: center; justify-content: center; gap: 40px;
  }
  .card {
    position: relative; width: 540px; height: 346px;
    box-shadow: 0 2px 10px rgba(0,0,0,0.08);
  }
  .card--back { background: var(--paper); border: 1px solid var(--edge); }
  .card--front { background: var(--brand-blue); }

  .identity {
    position: absolute; right: 314px; top: 76px; text-align: right;
  }
  .identity__name {
    font-size: 21px; font-weight: 400; color: var(--ink); line-height: 1;
    display: flex; align-items: flex-end; justify-content: flex-end; gap: 4px;
  }
  .identity__name strong { font-weight: 700; }
  .identity__role { font-size: 11.5px; color: var(--ink); margin-top: 4px; }

  .credentials {
    position: absolute; left: 238px; top: 85px;
    font-size: 11.5px; line-height: 16px; color: var(--muted);
  }
  .credentials b { font-weight: 700; }

  .phone {
    position: absolute; left: 195px; top: 165px;
    display: flex; align-items: center; gap: 6px;
    font-size: 17px; font-weight: 700; color: var(--ink);
  }
  .online {
    position: absolute; right: 54px; top: 224px;
    display: flex; align-items: center; gap: 8px;
  }
  .online__lines { font-size: 15.5px; line-height: 21px; color: var(--ink); }
  .online__lines .web { font-weight: 700; }

  .brand {
    position: absolute; left: 80px; top: 128px;
    display: flex; align-items: center; gap: 28px;
  }
  .brand__dot {
    width: 74px; height: 74px; border-radius: 50%; background: var(--paper);
  }
  .brand__name {
    font-size: 38px; font-weight: 300; color: var(--paper); letter-spacing: 0.2px;
  }
</style>
</head>
<body>
<main class="sheet">
  <section class="card card--back" aria-label="Card back">
    <div class="identity">
      <div class="identity__name">
        <svg width="16" height="20" viewBox="0 0 16 20" aria-hidden="true">
          <circle cx="8" cy="6" r="4.5" fill="none" stroke="var(--brand-blue)" stroke-width="1.4"/>
          <path d="M1 19 v-3 a7 6 0 0 1 14 0 v3 z" fill="none" stroke="var(--brand-blue)" stroke-width="1.4"/>
        </svg>
        <span>Derek <strong>Hollis</strong></span>
      </div>
      <div class="identity__role">Counsellor &amp; Psychotherapist</div>
    </div>
    <div class="credentials">
      <div><b>BSc</b> (Psychol.) | <b>BA, Dip.</b> (Couns. &amp; Psych.)</div>
      <div><b>PG.Cert</b> (CBT) | <b>MGVrA, NWTF</b></div>
    </div>
    <div class="phone">
      <svg width="12" height="20" viewBox="0 0 12 20" aria-hidden="true">
        <rect x="1" y="1" width="10" height="18" rx="1.8" fill="none" stroke="var(--brand-blue)" stroke-width="1.4"/>
        <line x1="4.5" y1="16" x2="7.5" y2="16" stroke="var(--brand-blue)" stroke-width="1.2"/>
      </svg>
      <span>087 5550 142</span>
    </div>
    <div class="online">
      <svg width="20" height="20" viewBox="0 0 20 20" aria-hidden="true">
        <g fill="none" stroke="var(--brand-blue)" stroke-width="1.2">
          <circle cx="10" cy="10" r="8.5"/>
          <ellipse cx="10" cy="10" rx="4" ry="8.5"/>
          <line x1="1.5" y1="10" x2="18.5" y2="10"/>
          <path d="M3 5.5 h14 M3 14.5 h14"/>
        </g>
      </svg>
      <div class="online__lines">
        <div class="web">www.harborlane.ie</div>
        <div>info@harborlane.ie</div>
      </div>
    </div>
  </section>

  <section class="card card--front" aria-label="Card front">
    <div class="brand">
      <div class="brand__dot"></div>
      <div class="brand__name">Harbor Lane</div>
    </div>
  </section>
</main>
</body>
</html>
```